Recycling Exhibition Web Design Project

We are developing a new website for a exhibition we have just taken over. The previous site is very basic and we require a complete redesign. The site should be designed to engage with and attract those who work in or provide services to the multibillion dollar wastes and recycling industry in the Asia pacific region. These will include Federal & State Governments, City councils, private sector, industry associations and other key bodies, education facilities.

KTLO is the premier waste and recycling event in the Asia Pacific region and known as place where the industry meets to share innovations, gain knowledge, to network and do business.
• Innovation
• Knowledge transfer
• Industry Networking
• Trade
Key point: need to reflect that 2012 show will attract large numbers of quality visitors from across wide range of the industry – city councils, facilities managers, etc

Site should deliver 3 key objectives.
1. Stimulate interest those who work in or provide services to the wastes and recycling industry by providing simple to access, relevant and topical information about the Expo, the Seminars, the Key Features, the sub activities and the key benefits to them.
2. Provide a platform that supports / improves EP by providing a range of interactive components – ie floor plan / video. In addition options for sales enquiries, registration, general feedback
3. Provide a way to highlight / showcase sponsors, show features and other key assets. (possibly a carousel above the fold)

We really like the dunmar website so a take on this could be good (http://www.dunmar-example.com.au/). Also we want to try to reinforce the brand so we should use the event as the hero image/banner.

Previous website - http://www.ktlo-example.com.au/

Target Market(s)

The site should be designed to engage with and attract those who work in or provide services to the multibillion dollar wastes and recycling industry

Industry/Entity Type

Recycling

Requirements
Must have
• The icons on the current site work quite well so inclusion as CTAs would be preferable.

Other key areas are

• Seminar Delegate & Visitor Registration
• Exhibitor Prospectus
• Floorplan
• Conference / Seminar content
• Social media + blog

Site visitors will need to feel like they are part of a community.
Site should reflect/display key industry stats & stats from 2011 expo

Please see the attached brief for more details and site map for menu items.

```html
<!DOCTYPE html>
<html lang="en">
<head>
<meta charset="utf-8">
<title>KTLO Expo 2012</title>
<link rel="stylesheet" href="https://fonts.googleapis.com/css2?family=Oswald:wght@400;500&family=Arimo:wght@400;700&display=swap">
<style>
:root{
  --ink:#1f1f1f;
  --header:#252525;
  --nav:#111;
  --lime:#d4d64a;
  --lime-panel:#c9cb4e;
  --lime-mid:#d2d36c;
  --olive-text:#56581e;
  --olive-sub:#6f7130;
  --white:#fff;
  --grey-band:#e4e4e4;
  --orange:#e88a1e;
  --red:#c8361e;
  --footer:#232323;
}
*{margin:0;padding:0;box-sizing:border-box}
html,body{width:1200px;height:989px;overflow:hidden;background:var(--header);font-family:"Arimo",Arial,sans-serif;color:var(--ink)}
.page{position:relative;width:1200px;height:989px}
.header{position:absolute;left:0;top:0;width:1200px;height:152px;background:var(--header)}
.brand{position:absolute;display:flex;align-items:center;gap:12px}
.brand-name{font-family:"Oswald",sans-serif;font-weight:500;color:var(--white);font-size:40px;line-height:1;white-space:nowrap}
.brand-dot{width:34px;height:34px;border-radius:50%;background:var(--orange)}
.header .brand{left:66px;top:52px}
.top-links{position:absolute;right:20px;top:10px;display:flex;align-items:center;height:24px}
.top-links a{color:#e6e6e6;font-size:12px;text-decoration:none;padding:0 14px;border-right:1px solid #444;line-height:20px}
.top-links .ico{padding:0 14px;border-right:1px solid #444;display:flex;align-items:center;height:20px}
.top-links .ico:last-child{border-right:0}
.sq{width:14px;height:14px;background:#e6e6e6;border-radius:2px}
.enquiries{position:absolute;right:16px;top:80px;font-family:"Oswald",sans-serif;font-size:20px;color:var(--lime);white-space:nowrap}
.enquiries span{margin-left:10px}
.nav{position:absolute;left:0;top:152px;width:1200px;height:41px;background:linear-gradient(#3a3a3a,#0c0c0c 55%,#000)}
.nav ul{list-style:none;display:flex;height:41px}
.nav li{height:41px;display:flex;align-items:center;justify-content:center;color:var(--white);font-size:12px;font-weight:700;border-right:1px solid #444;white-space:nowrap}
.search{position:absolute;left:976px;top:3px;width:211px;height:34px;border-radius:17px;background:#262626;box-shadow:inset 0 1px 3px #000;display:flex;align-items:center;padding-left:14px;gap:10px;color:#9a9a9a;font-size:12px}
.hero-info{position:absolute;left:0;top:193px;width:368px;height:317px;background:radial-gradient(circle at 45% 45%,#5a5a5a,#2b2b2b 70%)}
.hero-date{position:absolute;left:36px;top:44px;font-family:"Oswald",sans-serif;font-size:33px;line-height:44px;color:var(--lime);text-shadow:0 2px 3px #000;white-space:nowrap;letter-spacing:-.3px}
.hero-venue{position:absolute;left:36px;top:114px;font-family:"Oswald",sans-serif;font-size:20px;line-height:31px;color:var(--lime);text-shadow:0 2px 3px #000;white-space:nowrap}
.hero-image{position:absolute;left:368px;top:193px;width:832px;height:236px;background:linear-gradient(#c7d23a 0%,#f2f07a 38%,#a7b83a 62%,#6aa62a 80%,#58a61e 100%)}
.categories{position:absolute;left:368px;top:429px;width:832px;height:81px;display:flex;background:linear-gradient(#3b3b3b,#1e1e1e)}
.cat{flex:1;border-right:1px solid #4a4a4a;display:flex;flex-direction:column;align-items:center;justify-content:flex-end;padding-bottom:8px;color:var(--white);font-size:9.5px;font-weight:700;text-align:center;line-height:11px;gap:6px;white-space:nowrap}
.cat:last-child{border-right:0}
.cat svg{width:34px;height:34px}
.content{position:absolute;left:0;top:510px;width:1200px;height:267px}
.topics{position:absolute;left:0;top:0;width:368px;height:267px;background:var(--lime-panel)}
.section-title{font-family:"Oswald",sans-serif;font-weight:400;font-size:24px;color:#2a2a1a;white-space:nowrap}
.topics .section-title{position:absolute;left:36px;top:20px}
.topic-list{position:absolute;left:36px;top:63px;width:300px;list-style:none;border-top:1px solid #b1b33a}
.topic-list li{font-size:14.5px;font-weight:700;color:#3b3d14;padding:10px 2px;border-bottom:1px solid #b1b33a;line-height:18px;white-space:nowrap}
.program{position:absolute;left:368px;top:0;width:555px;height:267px;background:var(--lime-mid)}
.program .section-title{position:absolute;left:34px;top:20px}
.program .section-title small{font-size:17px;color:var(--olive-text);margin-left:6px}
.program-list{position:absolute;left:34px;top:62px;width:450px;list-style:none}
.program-list li{padding:7px 0 6px;border-bottom:1px solid #b9bb52;line-height:17px;white-space:nowrap}
.program-list li:first-child{border-top:1px solid #b9bb52}
.program-list strong{display:block;font-size:15px;color:var(--olive-text);letter-spacing:.3px}
.program-list span{font-size:13.5px;color:var(--olive-sub)}
.gallery{position:absolute;left:923px;top:0;width:277px;height:267px;background:var(--lime-panel)}
.video{position:absolute;left:27px;top:21px;width:230px;height:129px;border:3px solid #d9d9d9;background:linear-gradient(#1c1c1c,#3a4a4a 60%,#1a1a1a);box-shadow:0 1px 3px #555}
.gallery-title{position:absolute;left:0;width:277px;text-align:center;top:172px;font-family:"Oswald",sans-serif;font-size:25px;color:#2a2a1a;white-space:nowrap}
.gallery-sub{position:absolute;left:0;width:277px;text-align:center;top:207px;font-family:"Oswald",sans-serif;font-size:18px;color:var(--olive-text);white-space:nowrap}
.gallery-rule{position:absolute;left:30px;top:246px;width:222px;height:1px;background:#b1b33a}
.supporters{position:absolute;left:0;top:777px;width:1200px;height:64px;background:var(--grey-band);border-top:5px solid var(--orange);border-bottom:5px solid var(--red)}
.supporters-label{position:absolute;left:15px;top:22px;font-size:11px;font-weight:700;color:#333}
.supporter{position:absolute;top:12px;height:30px;background:#c3c3c3;border-radius:3px}
.footer{position:absolute;left:0;top:841px;width:1200px;height:148px;background:var(--footer);color:var(--white)}
.footer-col{position:absolute;top:22px}
.footer-col h3{font-family:"Oswald",sans-serif;font-weight:400;font-size:20px;margin-bottom:6px;white-space:nowrap}
.footer-col p{font-size:11px;line-height:16.5px;white-space:nowrap}
.footer-col .mail{color:#e2e27a}
.social{display:grid;grid-template-columns:110px 110px;font-size:11px;line-height:16.5px}
.social div{display:flex;align-items:center;gap:7px;white-space:nowrap}
.social i{width:10px;height:10px;background:#e6e6e6;border-radius:1px;display:inline-block}
.footer .brand{right:40px;top:48px}
.footer .brand-name{font-size:34px}
.footer .brand-dot{width:28px;height:28px}
</style>
</head>
<body>
<div class="page">
  <header class="header">
    <div class="brand"><span class="brand-dot"></span><span class="brand-name">KTLO Expo</span></div>
    <nav class="top-links">
      <a href="#">Login</a><a href="#">Register</a>
      <span class="ico"><span class="sq"></span></span>
      <span class="ico"><span class="sq"></span></span>
      <span class="ico"><span class="sq"></span></span>
      <span class="ico"><span class="sq"></span></span>
      <span class="ico"><span class="sq"></span></span>
      <span class="ico"><svg width="16" height="12" viewBox="0 0 16 12"><rect x="0.5" y="0.5" width="15" height="11" fill="#e6e6e6"/><path d="M1 1l7 6 7-6" stroke="#252525" stroke-width="1.4" fill="none"/></svg></span>
    </nav>
    <div class="enquiries">Enquiries:<span>61 (3) 9000 1234</span></div>
  </header>

  <nav class="nav">
    <ul>
      <li style="width:114px">Home</li>
      <li style="width:161px">About the Show</li>
      <li style="width:135px">What's On</li>
      <li style="width:122px">Register</li>
      <li style="width:183px">How to Exhibit</li>
      <li style="width:77px">Blog</li>
      <li style="width:131px">Contact Us</li>
    </ul>
    <div class="search">
      <svg width="14" height="14" viewBox="0 0 14 14"><circle cx="5.5" cy="5.5" r="4.3" stroke="#bbb" stroke-width="1.8" fill="none"/><path d="M8.7 8.7L13 13" stroke="#bbb" stroke-width="2"/></svg>
      Search
    </div>
  </nav>

  <section class="hero-info">
    <div class="hero-date">21 &amp; 22 November 2012</div>
    <div class="hero-venue">Harbourside Convention Centre<br>Sydney</div>
  </section>
  <div class="hero-image" role="img" aria-label="Wind turbines on a green field under a golden sunset sky"></div>

  <nav class="categories">
    <div class="cat"><svg viewBox="0 0 34 34"><path d="M17 3L32 30H2z" fill="none" stroke="#fff" stroke-width="2.5"/><circle cx="17" cy="21" r="4" fill="#fff"/></svg>HAZARDOUS<br>WASTE</div>
    <div class="cat"><svg viewBox="0 0 34 34"><rect x="8" y="8" width="18" height="18" transform="rotate(45 17 17)" fill="none" stroke="#fff" stroke-width="2.5"/><circle cx="17" cy="17" r="4" fill="#fff"/></svg>DISPOSAL</div>
    <div class="cat"><svg viewBox="0 0 34 34"><ellipse cx="17" cy="13" rx="10" ry="8" fill="#fff"/><rect x="8" y="22" width="18" height="6" rx="2" fill="#fff"/></svg>COMPOST</div>
    <div class="cat"><svg viewBox="0 0 34 34"><circle cx="17" cy="13" r="9" fill="none" stroke="#fff" stroke-width="2.5"/><rect x="13" y="23" width="8" height="7" fill="#fff"/></svg>ENERGY<br>FROM WASTE</div>
    <div class="cat"><svg viewBox="0 0 34 34"><path d="M9 8h16l-2 22H11z" fill="#fff"/><rect x="7" y="4" width="20" height="3" fill="#fff"/></svg>BIN LINERS<br>&amp; CONTAINERS</div>
    <div class="cat"><svg viewBox="0 0 34 34"><circle cx="11" cy="19" r="7" fill="none" stroke="#fff" stroke-width="3.5"/><circle cx="24" cy="12" r="6" fill="none" stroke="#fff" stroke-width="3.5"/></svg>MACHINERY<br>&amp; EQUIPMENT</div>
    <div class="cat"><svg viewBox="0 0 34 34"><path d="M3 7l13 3v19L3 26zM31 7l-13 3v19l13-3z" fill="#fff"/></svg>SERVICE &amp;<br>SOLUTIONS</div>
    <div class="cat"><svg viewBox="0 0 34 34"><rect x="2" y="9" width="20" height="15" fill="#fff"/><path d="M22 13h6l4 5v6H22z" fill="#fff"/><circle cx="9" cy="26" r="3" fill="#333" stroke="#fff" stroke-width="1.5"/><circle cx="26" cy="26" r="3" fill="#333" stroke="#fff" stroke-width="1.5"/></svg>VEHICLES<br>&amp; PLANT</div>
    <div class="cat"><svg viewBox="0 0 34 34"><path d="M17 4l6 10h-12zM5 28l6-10 6 10zM29 28H17l6-10z" fill="#fff"/></svg>RECYCLED<br>PRODUCTS</div>
  </nav>

  <main class="content">
    <section class="topics">
      <h2 class="section-title">KTLO Conference Topics</h2>
      <ul class="topic-list">
        <li>Impact of the Carbon Price &amp;<br>Carbon Farming Initiative</li>
        <li>Product Stewardship &amp; Innovation</li>
        <li>Waste to Energy &amp; Local Government<br>AWT Procurement</li>
        <li>Green Buildings</li>
      </ul>
    </section>
    <section class="program">
      <h2 class="section-title">2012 Exhibition Program<small>(See Full Program)</small></h2>
      <ul class="program-list">
        <li><strong>Carbon Price &amp; Carbon Farming Initiative</strong><span>Morning &nbsp;/&nbsp; $185 (GST incl.) &nbsp;/&nbsp; Includes lunch</span></li>
        <li><strong>Product Stewardship &amp; Innovation</strong><span>Afternoon &nbsp;/&nbsp; $99 (GST incl.) &nbsp;/&nbsp; Includes lunch</span></li>
        <li><strong>Waste to Energy &amp; Local Government AWT Procurement</strong><span>Morning &nbsp;/&nbsp; $99 (GST incl.) &nbsp;/&nbsp; Includes lunch</span></li>
        <li><strong>Green Buildings: Design, Construction &amp; Operation</strong><span>Afternoon / &nbsp;$99 (GST incl.) &nbsp;/&nbsp; Includes lunch</span></li>
      </ul>
    </section>
    <aside class="gallery">
      <div class="video" role="img" aria-label="Video of last year's exhibition stand with a play button">
        <svg width="224" height="123" viewBox="0 0 224 123"><circle cx="112" cy="56" r="16" fill="rgba(255,255,255,.35)"/><path d="M106 47l15 9-15 9z" fill="#fff"/><rect x="0" y="112" width="224" height="11" fill="#111"/><rect x="18" y="116" width="150" height="3" fill="#555"/></svg>
      </div>
      <div class="gallery-title">See Last Year's Exhibition</div>
      <div class="gallery-sub">(View images from this event)</div>
      <div class="gallery-rule"></div>
    </aside>
  </main>

  <section class="supporters">
    <div class="supporters-label">SUPPORTED BY:</div>
    <div class="supporter" style="left:140px;width:96px"></div>
    <div class="supporter" style="left:246px;width:34px"></div>
    <div class="supporter" style="left:295px;width:82px"></div>
    <div class="supporter" style="left:430px;width:104px"></div>
    <div class="supporter" style="left:580px;width:152px"></div>
    <div class="supporter" style="left:778px;width:46px"></div>
    <div class="supporter" style="left:858px;width:146px"></div>
    <div class="supporter" style="left:1042px;width:100px"></div>
  </section>

  <footer class="footer">
    <div class="footer-col" style="left:36px">
      <h3>Contact KTLO</h3>
      <p>Dana Price<br>Group Exhibition Director<br>p. +61 3 9000 1234<br>e. <span class="mail">dprice@northbay-example.com.au</span></p>
    </div>
    <div class="footer-col" style="left:261px">
      <h3>Address</h3>
      <p>Northbay Exhibitions<br>Level 3<br>88 Harbour Road<br>Melbourne VIC 3004</p>
    </div>
    <div class="footer-col" style="left:499px">
      <h3>Connect with Us</h3>
      <div class="social">
        <div><i></i>Community</div><div><i></i>Network</div>
        <div><i></i>Updates</div><div><i></i>Green Directory</div>
        <div><i></i>Video</div><div><i></i>Newsletter</div>
      </div>
    </div>
    <div class="brand"><span class="brand-dot"></span><span class="brand-name">KTLO Expo</span></div>
  </footer>
</div>
</body>
</html>
```